Rising Paths Web Design

I am starting a new company that will provide LIFE COACHING services - I have tried to design a website, but it's too complicated. Right now, it's just me - I'm the only person that will provide services through the website - I have used artmarket to purchase a logo (see below). I want to be able to update the website myself, but need a template - basic design. Because I am not technologically savvy enough to explain in words - I basically want to have a website that will provide basic information about my services (coaching), a page about me and my background, hopefully scheduling possibilities, and testimonials — also a page for writing/blogs. I bought a website through NetHarbor - so when I have a template, I guess I”d use that - but maybe I’ll need to work with a designer to actually get it up on the internet. I have a head shot that I’ll upload, too.
Target Market(s)
Clients from the independent (private school) world - teachers, administrators
Number of Pages Required
4 page
Look and feel
Each slider illustrates characteristics of the customer's brand and the style your logo design should communicate.

```html
<!DOCTYPE html>
<html lang="en">
<head>
<meta charset="utf-8">
<title>Rising Paths Coaching</title>
<link rel="stylesheet" href="https://fonts.googleapis.com/css2?family=Cinzel:wght@400;600&family=Montserrat:wght@400;500;600&display=swap">
<style>
:root{
  --teal:#1aa99b;
  --teal-dark:#11907f;
  --ink:#1d1d1d;
  --body:#555;
  --mist:#eeeeee;
  --paper:#ffffff;
  --night:#050505;
}
*{margin:0;padding:0;box-sizing:border-box}
html,body{width:1200px;height:3896px;overflow:hidden}
body{position:relative;background:var(--paper);font-family:'Montserrat',sans-serif;color:var(--ink)}
.abs{position:absolute}
.serif{font-family:'Cinzel',serif}
.btn{position:absolute;background:var(--teal);color:#fff;font:600 11px 'Montserrat',sans-serif;letter-spacing:.3px;display:flex;align-items:center;justify-content:center;border-radius:0 12px 0 12px;text-transform:uppercase}
.eyebrow{position:absolute;left:0;width:1200px;text-align:center;font:500 16px 'Montserrat',sans-serif;letter-spacing:4px;color:var(--teal)}
.section-title{position:absolute;left:0;width:1200px;text-align:center;font:400 31px 'Cinzel',serif;letter-spacing:1px;color:var(--ink)}
.rule{position:absolute;left:576px;width:48px;height:4px;background:var(--teal)}

/* header */
.site-header{position:absolute;top:0;left:0;width:1200px;height:66px;background:#fff;box-shadow:0 2px 6px rgba(0,0,0,.06);z-index:3}
.logo-badge{position:absolute;left:118px;top:0;width:100px;height:100px;border-radius:50%;background:#fff;box-shadow:0 3px 8px rgba(0,0,0,.12);z-index:4;display:flex;align-items:center;justify-content:center;flex-direction:column}
.logo-badge .name{font:400 11px 'Cinzel',serif;color:#333}
.logo-badge .sub{font:500 5px 'Montserrat',sans-serif;letter-spacing:2px;color:var(--teal);margin-top:2px}
.nav{position:absolute;top:0;left:293px;height:70px;display:flex;align-items:center;gap:0}
.nav a{font:500 11px 'Montserrat',sans-serif;color:#222;text-decoration:none;margin-right:52px}
.nav a.active{color:var(--teal)}
.header-cta{left:950px;top:18px;width:135px;height:36px;font-size:11px}

/* hero */
.hero-bg{position:absolute;top:66px;left:0;width:1200px;height:624px;background:linear-gradient(90deg,#f3f3f3,#e6e8e8);border-radius:0 0 0 170px}
.hero-photo{position:absolute;top:66px;left:580px;width:620px;height:624px;border-radius:190px 0 0 0;background:linear-gradient(135deg,#c7d0cd 0%,#a98564 40%,#8a5a33 60%,#4f7a72 100%)}
.hero-ring{position:absolute;left:8px;top:210px;width:420px;height:420px;border:1.5px solid rgba(26,169,155,.35);border-radius:50%}
.hero-kicker{left:90px;top:238px;font:500 20px 'Montserrat',sans-serif;letter-spacing:7px;color:var(--teal)}
.hero-title{left:88px;top:262px;font:600 59px/1.25 'Cinzel',serif;color:#151515}
.hero-text{left:90px;top:416px;width:520px;font:400 12px/22px 'Montserrat',sans-serif;color:#444}
.hero-cta{left:91px;top:473px;width:134px;height:37px}

/* services */
.card{position:absolute;top:975px;width:221px;height:240px;background:#fff;box-shadow:0 3px 12px rgba(0,0,0,.08);text-align:center}
.card .icon{position:absolute;left:65px;top:-45px;width:90px;height:90px;border-radius:50%;border:2px solid var(--teal);padding:5px}
.card .icon span{display:block;width:100%;height:100%;border-radius:50%;background:var(--teal)}
.card h3{position:absolute;top:62px;width:100%;font:400 14px 'Cinzel',serif;letter-spacing:.5px;color:#222}
.card .bar{position:absolute;top:85px;left:95px;width:30px;height:3px;background:var(--teal)}
.card p{position:absolute;top:102px;left:10px;width:201px;font:400 10.5px/22px 'Montserrat',sans-serif;color:#555}
.card .btn{left:44px;top:220px;width:134px;height:38px}

/* about */
.about-bg{position:absolute;top:1327px;left:0;width:1200px;height:655px;background:linear-gradient(90deg,#f4f4f4,#ececec)}
.about-frame{position:absolute;left:45px;top:1475px;width:542px;height:412px;border:4px solid var(--teal);border-radius:0 0 0 0}
.about-photo{position:absolute;left:56px;top:1483px;width:519px;height:396px;border-radius:0 190px 0 70px;background:linear-gradient(160deg,#d9d3c9 0%,#c6a676 40%,#e6e1d8 75%,#f3f1ec 100%)}
.about-kicker{left:640px;top:1475px;font:500 16px 'Montserrat',sans-serif;letter-spacing:4px;color:var(--teal)}
.about-title{left:640px;top:1500px;font:400 31px 'Cinzel',serif;color:#1d1d1d;letter-spacing:.5px}
.about-rule{position:absolute;left:640px;top:1549px;width:48px;height:4px;background:var(--teal)}
.about-text{left:640px;top:1574px;width:446px;font:400 11px/22px 'Montserrat',sans-serif;color:#555;text-align:justify}
.about-cta{left:640px;top:1829px;width:134px;height:37px}

/* testimonials */
.reviews-band{position:absolute;left:0;top:1982px;width:1200px;height:613px}
.reviews-kicker{top:2080px;color:#fff}
.reviews-title{top:2106px;color:#fff}
.reviews-rule{top:2154px;background:#fff}
.quote{position:absolute;width:400px;color:#fff}
.quote .mark{font:600 52px/1 'Cinzel',serif;height:40px}
.quote h4{font:400 20px/27px 'Cinzel',serif;letter-spacing:.5px;margin:8px 0 0 0}
.quote p{margin-top:18px;font:400 11px/22px 'Montserrat',sans-serif;text-align:justify;opacity:.95}
.quote cite{display:block;margin-top:8px;font:italic 400 13px 'Cinzel',serif;letter-spacing:.5px}
.arrow{position:absolute;top:2320px;width:20px;height:36px}

/* blog */
.post{position:absolute;top:2796px;width:297px;height:341px;background:#fff;box-shadow:0 3px 12px rgba(0,0,0,.1);text-align:center}
.post .thumb{position:absolute;left:6px;top:6px;width:285px;height:186px}
.post h4{position:absolute;top:216px;left:14px;width:269px;font:400 12.5px/20px 'Cinzel',serif;color:#222;letter-spacing:.3px}
.post p{position:absolute;top:260px;left:18px;width:261px;font:400 10.5px/21px 'Montserrat',sans-serif;color:#555}

/* newsletter */
.news-bg{position:absolute;left:0;top:3218px;width:1200px;height:315px;background:linear-gradient(90deg,#f4f4f4,#ebebeb)}
.news-input{position:absolute;left:300px;top:3410px;width:393px;height:38px;border:1px solid #888;border-radius:0 14px 0 14px;background:#fff;font:italic 400 11px 'Montserrat',sans-serif;color:#444;padding:13px 0 0 22px}
.news-btn{left:699px;top:3410px;width:201px;height:38px;font-size:13px;letter-spacing:1px}

/* footer */
.footer-shape{position:absolute;left:0;top:3528px;width:1200px;height:368px}
.footer-logo{position:absolute;left:150px;top:3640px;width:136px;height:86px;display:flex;flex-direction:column;align-items:center;justify-content:center;color:#fff}
.footer-logo .mark{width:100px;height:100px;border:1.5px solid var(--teal);border-radius:50%;position:absolute;left:18px;top:-7px}
.footer-logo .name{font:400 15px 'Cinzel',serif;position:relative}
.footer-logo .sub{font:500 7px 'Montserrat',sans-serif;letter-spacing:3px;color:var(--teal);position:relative;margin-top:3px}
.fcol{position:absolute;top:3614px;color:#fff}
.fcol h5{font:400 13px 'Cinzel',serif;letter-spacing:.5px;margin-bottom:11px}
.fcol li{list-style:none;font:400 10.5px/22px 'Montserrat',sans-serif;color:#eee;padding-left:20px;position:relative}
.fcol li::before{content:'»';position:absolute;left:0;color:var(--teal)}
.contact-item{position:absolute;left:871px;display:flex;align-items:flex-start;color:#eee;font:400 10.5px/20px 'Montserrat',sans-serif}
.contact-item svg{flex:none;margin-right:12px}
.footer-rule{position:absolute;left:114px;top:3795px;width:964px;height:1px;background:#555}
.copyright{position:absolute;left:0;top:3824px;width:1200px;text-align:center;font:400 10px 'Montserrat',sans-serif;color:#eee}
.socials{position:absolute;left:532px;top:3852px;display:flex;gap:12px}
.socials span{width:22px;height:22px;border:1.5px solid var(--teal);border-radius:50%}
</style>
</head>
<body>

<header class="site-header">
  <nav class="nav">
    <a class="active" style="margin-right:60px">HOME</a>
    <a>ABOUT ME</a>
    <a>SERVICES</a>
    <a>TESTIMONIALS</a>
    <a>BLOG</a>
    <a>CONTACT ME</a>
  </nav>
  <div class="btn header-cta">Schedule Now</div>
</header>
<div class="logo-badge"><span class="name">RISING PATHS</span><span class="sub">COACHING</span></div>

<!-- hero -->
<div class="hero-bg"></div>
<div class="hero-ring"></div>
<div class="hero-photo" role="img" aria-label="Portrait of a smiling coach in glasses holding a folder in an office"></div>
<div class="abs hero-kicker">WELCOME TO</div>
<h1 class="abs hero-title">RISING PATHS<br>COACHING</h1>
<p class="abs hero-text">Lorem ipsum dolor sit amet, consectetur adipiscing elit, sed do eiusmod tempor incidi dunt ut labore et dolore magna aliqua.</p>
<div class="btn hero-cta">Schedule Now</div>

<!-- services -->
<div class="eyebrow" style="top:805px">OUR COACHING SERVICES</div>
<h2 class="section-title" style="top:829px">WHAT WE DO</h2>
<div class="rule" style="top:878px"></div>

<div class="card" style="left:130px"><div class="icon" role="img" aria-label="Career coaching icon"><span></span></div><h3>CAREER COACHING</h3><div class="bar"></div><p>Lorem ipsum dolor sit amet, cons ectetur adipiscing elit, sed do eiu smod tempor incididunt ut labore et dolore magna aliqua. Quis ipsum suspendisse ultrices gravida.</p><div class="btn">Learn More</div></div>
<div class="card" style="left:370px"><div class="icon" role="img" aria-label="Health coaching icon"><span></span></div><h3>HEALTH COACHING</h3><div class="bar"></div><p>Lorem ipsum dolor sit amet, cons ectetur adipiscing elit, sed do eiu smod tempor incididunt ut labore et dolore magna aliqua. Quis ipsum suspendisse ultrices gravida.</p><div class="btn">Learn More</div></div>
<div class="card" style="left:610px"><div class="icon" role="img" aria-label="Business coaching icon"><span></span></div><h3>BUSINESS COACHING</h3><div class="bar"></div><p>Lorem ipsum dolor sit amet, cons ectetur adipiscing elit, sed do eiu smod tempor incididunt ut labore et dolore magna aliqua. Quis ipsum suspendisse ultrices gravida.</p><div class="btn">Learn More</div></div>
<div class="card" style="left:850px"><div class="icon" role="img" aria-label="Financial coaching icon"><span></span></div><h3>FINANCIAL COACHING</h3><div class="bar"></div><p>Lorem ipsum dolor sit amet, cons ectetur adipiscing elit, sed do eiu smod tempor incididunt ut labore et dolore magna aliqua. Quis ipsum suspendisse ultrices gravida.</p><div class="btn">Learn More</div></div>

<!-- about -->
<div class="about-bg"></div>
<svg class="abs" style="left:40px;top:1470px" width="560" height="420" viewBox="0 0 560 420">
  <path d="M5 415 V10 H340" fill="none" stroke="#1aa99b" stroke-width="5"/>
  <path d="M5 415 H545 V130" fill="none" stroke="#1aa99b" stroke-width="5"/>
</svg>
<div class="about-photo" role="img" aria-label="Headshot of the coach, a smiling woman with short blonde hair in a cream sweater"></div>
<div class="abs about-kicker">ABOUT ME</div>
<h2 class="abs about-title">HELLO I AM MAREN HOLT</h2>
<div class="about-rule"></div>
<p class="abs about-text">Lorem ipsum dolor sit amet, consectetur adipiscing elit, sed do eiusmod tempor incididunt ut labore et dolore magna aliqua. Quis ipsum suspendisse ultrices gravida. Risus commodo viverra maecenas accumsan lacus vel facilisis. perspiciatis unde omnis iste natus error sit voluptatem accusantium doloremque laudantium, totam rem aperiam, eaque ipsa quae ab illo inventore veritatis et quasi architecto beatae vitae dicta sunt explicabo. Nemo enim ipsam voluptatem quia voluptas sit aspernatur aut odit aut fugit, sed quia consequuntur magni dolores eos qui ratione voluptatem sequi nesciunt. Neque porro quisquam est, qui dolorem ipsum quia dolor sit amet, consectetur, adipisci velit, sed quia non numquam eius modi tempora incidunt ut labore et dolore magnam aliquam quaerat voluptatem.</p>
<div class="btn about-cta">Learn More</div>

<!-- testimonials -->
<svg class="reviews-band" viewBox="0 0 1200 613" role="img" aria-label="Teal testimonials band over a faint photo of a client writing">
  <defs>
    <linearGradient id="bandFill" x1="0" x2="1">
      <stop offset="0" stop-color="#3fb3a6"/>
      <stop offset=".5" stop-color="#1aa99b"/>
      <stop offset="1" stop-color="#1aa99b"/>
    </linearGradient>
  </defs>
  <rect width="1200" height="613" fill="#f5f5f5"/>
  <path d="M0 0 H1010 Q1200 0 1200 190 V613 H0 Z" fill="url(#bandFill)"/>
  <path d="M0 130 V470 Q0 580 120 595 L1200 600" fill="none" stroke="#fff" stroke-width="3"/>
  <path d="M900 8 Q1180 30 1200 210" fill="none" stroke="#fff" stroke-width="3"/>
</svg>
<div class="eyebrow reviews-kicker">OUR REVIEWS</div>
<h2 class="section-title reviews-title">OUR CLIENT TESTIMONIALS</h2>
<div class="rule reviews-rule"></div>

<svg class="arrow" style="left:48px" viewBox="0 0 20 36"><path d="M17 2 L3 18 L17 34" fill="none" stroke="#fff" stroke-width="2"/></svg>
<svg class="arrow" style="left:1133px" viewBox="0 0 20 36"><path d="M3 2 L17 18 L3 34" fill="none" stroke="#fff" stroke-width="2"/></svg>

<blockquote class="quote" style="left:136px;top:2210px">
  <div class="mark">“</div>
  <h4>LOREM IPSUM DOLOR SIT AMET CONS ECTETUR ADIPISCING.</h4>
  <p>Sed ut perspiciatis unde omnis iste natus error sit voluptatem accusantium doloremque laudantium, totam rem aperiam, eaque ipsa quae ab illo inventore veritatis et quasi architecto beatae vitae dicta sunt explicabo. Nemo enim ipsam voluptatem quia voluptas sit aspernatur aut odit aut fugit sed quia consequuntur.</p>
  <cite>- LILA BROOK</cite>
</blockquote>
<blockquote class="quote" style="left:639px;top:2210px">
  <div class="mark">“</div>
  <h4>LOREM IPSUM DOLOR SIT AMET CONS ECTETUR ADIPISCING.</h4>
  <p>Sed ut perspiciatis unde omnis iste natus error sit voluptatem accusantium doloremque laudantium, totam rem aperiam, eaque ipsa quae ab illo inventore veritatis et quasi architecto beatae vitae dicta sunt explicabo. Nemo enim ipsam voluptatem quia voluptas sit aspernatur aut odit aut fugit sed quia consequuntur.</p>
  <cite>- LILA BROOK</cite>
</blockquote>

<!-- blog -->
<div class="eyebrow" style="top:2693px">OUR BLOG</div>
<h2 class="section-title" style="top:2717px">OUR RECENT BLOG</h2>
<div class="rule" style="top:2767px"></div>

<article class="post" style="left:130px"><div class="thumb" role="img" aria-label="Two women talking in a bright living room" style="background:linear-gradient(135deg,#e8e4df,#b06a4a 55%,#f0ece6)"></div><h4>LOREM IPSUM DOLOR SIT AMET CONSEC TETUR ADIPISCING ELIT SED.</h4><p>Lorem ipsum dolor sit amet, consectetur adipi-scing elit, sed do eiusmod tempor incididunt ut labore et dolore magna aliqua.</p></article>
<article class="post" style="left:449px"><div class="thumb" role="img" aria-label="Coach meeting a client at a desk" style="background:linear-gradient(135deg,#eae6e0,#8aa3c4 50%,#5a4a40)"></div><h4>LOREM IPSUM DOLOR SIT AMET CONSEC TETUR ADIPISCING ELIT SED.</h4><p>Lorem ipsum dolor sit amet, consectetur adipi-scing elit, sed do eiusmod tempor incididunt ut labore et dolore magna aliqua.</p></article>
<article class="post" style="left:769px"><div class="thumb" role="img" aria-label="Two women in conversation at a table" style="background:linear-gradient(135deg,#d8d6d4,#c9a3b0 45%,#dfe4ec)"></div><h4>LOREM IPSUM DOLOR SIT AMET CONSEC TETUR ADIPISCING ELIT SED.</h4><p>Lorem ipsum dolor sit amet, consectetur adipi-scing elit, sed do eiusmod tempor incididunt ut labore et dolore magna aliqua.</p></article>

<!-- newsletter -->
<div class="news-bg"></div>
<div class="eyebrow" style="top:3302px">NEWSLETTER</div>
<h2 class="section-title" style="top:3326px">SUBSCRIBE OUR NEWSLETTER</h2>
<div class="rule" style="top:3375px"></div>
<div class="news-input">Enter Your Email</div>
<div class="btn news-btn">Sign Me Up!</div>

<!-- footer -->
<svg class="footer-shape" viewBox="0 0 1200 368">
  <path d="M0 10 H900 Q1130 10 1200 100 V368 H0 Z" fill="#050505"/>
  <path d="M0 8 H900 Q1130 8 1200 98" fill="none" stroke="#1aa99b" stroke-width="4"/>
</svg>
<div class="footer-logo"><span class="mark"></span><span class="name">RISING PATHS</span><span class="sub">COACHING</span></div>

<div class="fcol" style="left:337px"><h5>QUICK LINKS</h5><ul><li>Home</li><li>About Me</li><li>Services</li><li>Testimonials</li><li>Blog</li><li>Contact Me</li></ul></div>
<div class="fcol" style="left:496px"><h5>OUR SERVICES</h5><ul><li>Business Coaching</li><li>Health Coaching</li><li>Career Coaching</li><li>Financial Coaching</li></ul></div>
<div class="fcol" style="left:676px"><h5>IMPORTANT</h5><ul><li>Privacy &amp; Policy</li><li>Term and Conditions</li><li>Disclaimer</li><li>FAQ</li></ul></div>
<div class="fcol" style="left:871px"><h5>CONTACT US</h5></div>

<div class="contact-item" style="top:3648px">
  <svg width="22" height="22" viewBox="0 0 22 22"><circle cx="11" cy="11" r="10" fill="none" stroke="#1aa99b" stroke-width="1.5"/><path d="M11 5.5a3.5 3.5 0 0 0-3.5 3.5c0 2.6 3.5 6.5 3.5 6.5s3.5-3.9 3.5-6.5A3.5 3.5 0 0 0 11 5.5z" fill="#1aa99b"/><circle cx="11" cy="9" r="1.2" fill="#050505"/></svg>
  <span>123 Lorem ipsum dolor sit amet,<br>consectetur adipiscing elit.</span>
</div>
<div class="contact-item" style="top:3700px">
  <svg width="22" height="22" viewBox="0 0 22 22"><circle cx="11" cy="11" r="10" fill="none" stroke="#1aa99b" stroke-width="1.5"/><path d="M7.5 6.5l2 -.5 1.2 2.6-1.2.9a6 6 0 0 0 2.9 2.9l.9-1.2 2.6 1.2-.5 2c-4.5.3-8.2-3.4-7.9-7.9z" fill="#1aa99b"/></svg>
  <span style="margin-top:1px">555 014 2286</span>
</div>
<div class="contact-item" style="top:3737px">
  <svg width="22" height="22" viewBox="0 0 22 22"><circle cx="11" cy="11" r="10" fill="none" stroke="#1aa99b" stroke-width="1.5"/><rect x="6" y="7.5" width="10" height="7" fill="#1aa99b"/><path d="M6 7.5l5 4 5-4" fill="none" stroke="#050505" stroke-width="1"/></svg>
  <span style="margin-top:1px">hello@risingpathsmail.com</span>
</div>

<div class="footer-rule"></div>
<p class="copyright">© copyrights 2022 Rising Paths Coaching &nbsp;&nbsp;|&nbsp;&nbsp;&nbsp; All rights reserved.</p>
<div class="socials" aria-label="Social links"><span></span><span></span><span></span><span></span></div>

</body>
</html>
```